Jewelry Business card for general purpose. Elegant and simple

We are a jewelry group with 6 stores in Mexico and 30 years in business.

We need a BC that at leats includes the name, mail, phone number and physical location (street, municipality, and county; example "Paseo Olmeda 2140", "Avenida Sotillo", "Monterrey").
Optional: we are trying to reposition the brand with the association of life-events or moments and family. Such as: birth, marriage, graduation, birthdays. Christmast, mothers day and fathers day.

We are looking for something elegant but simple

Jewelry name: "Lunetti". Email: "lunettibrillo@correo-ejemplo.mx". Phone num "4172-3095".

Target Market(s)

General business card: from suppliers to clients. One segment outstand: couples gettineg married

Industry/Entity Type

Jewelry Store

Contact Information for Business Card

Loking for something simple but elegant.

Font styles to use
Decorative
Script

Requirements
Must have
• Must have name, address, and mail.
Nice to have
• It could have jewelry pictures/design. Maybe quotes. Or general words as background . currently we have a very simple card with one ring would like to see something different.
Should not have
• Include real people.

```html
<!DOCTYPE html>
<html lang="en">
<head>
<meta charset="utf-8">
<title>Lunetti – Business Card</title>
<link rel="stylesheet" href="https://fonts.googleapis.com/css2?family=Great+Vibes&family=Open+Sans:wght@400&display=swap">
<style>
  :root {
    --backdrop: #dcdcdc;
    --card-black: #1d1d1d;
    --panel-black: #1f1f1f;
    --tan: #c3966b;
    --gold: #c39566;
    --gold-line: #a8845c;
    --text-light: #e6e3df;
  }
  html, body {
    margin: 0;
    padding: 0;
    width: 1200px;
    height: 746px;
    overflow: hidden;
    background: var(--backdrop);
  }
  .canvas {
    position: relative;
    width: 1200px;
    height: 746px;
  }
  .card {
    position: absolute;
    left: 100px;
    top: 88px;
    width: 1000px;
    height: 570px;
    background: var(--card-black);
    box-shadow: 0 6px 18px rgba(0,0,0,0.18);
  }
  .card__band {
    position: absolute;
    inset: 34px;
    background: var(--tan);
  }
  .card__panel {
    position: absolute;
    inset: 98px;
    background: var(--panel-black);
  }
  .card__frame {
    position: absolute;
    inset: 24px;
    border: 1px solid var(--gold-line);
  }
  .card__content {
    position: absolute;
    inset: 0;
    display: flex;
    flex-direction: column;
    align-items: center;
    justify-content: center;
    text-align: center;
  }
  .card__name {
    margin: 0 0 10px;
    font-family: "Great Vibes", cursive;
    font-weight: 400;
    font-size: 86px;
    line-height: 1;
    color: var(--gold);
  }
  .card__line {
    margin: 0;
    font-family: "Open Sans", sans-serif;
    font-size: 17px;
    letter-spacing: 1.4px;
    color: var(--text-light);
  }
  .card__line + .card__line {
    margin-top: 26px;
  }
  .card__sep {
    margin: 0 8px;
  }
</style>
</head>
<body>
<main class="canvas">
  <section class="card" aria-label="Lunetti business card">
    <div class="card__band"></div>
    <div class="card__panel">
      <div class="card__frame"></div>
      <div class="card__content">
        <h1 class="card__name">Lunetti</h1>
        <p class="card__line">Email: lunettibrillo@correo-ejemplo.mx<span class="card__sep">|</span>Phone:4172-3095</p>
        <p class="card__line">Address: Paseo Olmeda No.2140. Local6 Avenida Sotillo</p>
      </div>
    </div>
  </section>
</main>
</body>
</html>
```